Would like to reproduce this screen to look more modern

My app is a place for farmers to post jobs a when needing help around the Farm, and local farmhands can apply for the job. The Farmer can then review multiple applicants and select the one best fit for the task at hand. I'm trying to give my screens an updated look while keeping my current color scheme and flow. I would like for you guys to recreate this screen with an updated look the best you can. The main screen with the PX will stay the same. I put that in there to show our logo and our main colors. They look outdated. the other 2 screens are looking at the customers profile, and the screen that u fill out to post a new job.

Target Market(s)

Farmers and farm employees inside the US

Industry/Entity Type

Agriculture

Requirements
Must have
• the same components for the flow but a new look
Nice to have
• ...
Should not have
• Should not change any features, but we can change how buttons look

```html
<!DOCTYPE html>
<html lang="en">
<head>
<meta charset="utf-8">
<title>Harvestly – App Screens</title>
<link href="https://fonts.googleapis.com/css2?family=Poppins:wght@400;500;600;700&display=swap" rel="stylesheet">
<style>
:root{
  --page:#e6e8e4;
  --screen:#ffffff;
  --surface:#f6f8f4;
  --green:#5a9b43;
  --green-dark:#2f6a2b;
  --green-soft:#e8f2e1;
  --grad-top:#9cc64f;
  --grad-bottom:#5fa84a;
  --ink:#1f2a1c;
  --body:#3c4639;
  --muted:#9aa396;
  --line:#e7ebe4;
  --icon:#9aa396;
  --heart:#e04848;
  --star:#f4b223;
}
*{box-sizing:border-box;margin:0;padding:0}
html,body{width:761px;height:1200px;overflow:hidden;background:var(--page);font-family:"Poppins",sans-serif;color:var(--ink)}
.abs{position:absolute}
.screen{position:absolute;width:278px;height:495px;background:var(--screen);overflow:hidden;border-radius:22px;box-shadow:0 10px 28px rgba(40,60,30,.14)}

/* splash */
.splash{left:86px;top:102px;background:linear-gradient(165deg,var(--grad-top),var(--grad-bottom))}
.splash-mark{left:96px;top:176px;width:86px;height:86px;border-radius:26px;background:var(--green-dark);box-shadow:0 12px 24px rgba(20,60,20,.28)}
.splash-name{left:0;top:282px;width:278px;text-align:center;color:#fff;font-weight:600;font-size:28px;letter-spacing:2px}

/* shared header */
.title{font-weight:600;font-size:12px;color:var(--ink)}
.back{left:16px;top:20px;width:28px;height:28px;border-radius:10px;background:#fff;box-shadow:0 2px 8px rgba(40,60,30,.1);display:flex;align-items:center;justify-content:center}
.avatar{border-radius:50%;background:radial-gradient(circle at 45% 40%,#c89a62,#5b4630)}

/* home */
.home{left:381px;top:102px;background:var(--surface)}
.tabs{left:16px;top:58px;width:246px;height:28px;border-radius:14px;background:var(--green-soft);display:flex;padding:3px}
.tab{flex:1;border-radius:11px;font-size:8px;display:flex;align-items:center;justify-content:center;color:var(--muted);font-weight:500}
.tab.active{background:#fff;color:var(--green);font-weight:600;box-shadow:0 2px 6px rgba(40,80,30,.12)}
.search{left:16px;top:94px;width:246px;height:28px;border-radius:12px;background:#fff;border:1px solid var(--line);display:flex;align-items:center;padding:0 4px 0 10px;font-size:7px;color:var(--muted);gap:6px}
.filter{margin-left:auto;width:20px;height:20px;border-radius:8px;background:var(--green);display:flex;align-items:center;justify-content:center}
.list{left:0;top:130px;width:278px;height:365px;overflow:hidden}
.job{left:16px;width:246px;height:72px;background:#fff;border-radius:14px;box-shadow:0 3px 10px rgba(40,60,30,.07)}
.job-icon{left:10px;top:9px;width:32px;height:32px;border-radius:11px;background:var(--green-soft);display:flex;align-items:center;justify-content:center}
.job-title{left:50px;top:8px;font-size:9px;font-weight:600;color:var(--green);line-height:1.2}
.job-meta{left:50px;font-size:6.2px;color:var(--muted);line-height:1}
.job-heart{left:212px;top:10px;width:24px;height:24px;border-radius:50%;background:#f4f6f2;display:flex;align-items:center;justify-content:center}
.job-rule{left:10px;top:47px;width:226px;height:1px;background:var(--line)}
.rate{left:10px;top:54px;height:14px;border-radius:7px;background:var(--green-soft);padding:0 7px;display:flex;align-items:center;font-size:6.2px;color:var(--muted)}
.rate b{color:var(--green);font-weight:600;margin-left:4px}
.dates{left:158px;top:51px;width:78px;font-size:6.2px;color:var(--muted);line-height:1.4}
.dates span{float:right;color:var(--body)}
.nav{left:14px;top:446px;width:250px;height:40px;border-radius:20px;background:#fff;box-shadow:0 6px 18px rgba(40,60,30,.16);display:flex;justify-content:space-around;align-items:center;padding:0 6px}
.nav-active{width:30px;height:30px;border-radius:50%;background:var(--green);display:flex;align-items:center;justify-content:center}

/* profile */
.profile{left:88px;top:612px;background:var(--surface)}
.banner{left:14px;top:58px;width:250px;height:78px;border-radius:18px;background:linear-gradient(135deg,#6aab4e,var(--green-dark));box-shadow:0 6px 16px rgba(47,106,43,.25)}
.online{left:58px;top:76px;width:8px;height:8px;border-radius:50%;background:#8fd15a;border:1.5px solid #fff}
.p-name{left:80px;top:74px;color:#fff;font-weight:600;font-size:11.5px;line-height:1.2}
.p-sub{left:80px;color:#e9f4e2;font-size:6.8px;line-height:1}
.rating{left:218px;top:72px;height:16px;border-radius:8px;padding:0 6px;background:rgba(255,255,255,.2);color:#fff;font-size:7px;display:flex;gap:3px;align-items:center}
.group{left:14px;width:250px;background:#fff;border-radius:14px;box-shadow:0 3px 10px rgba(40,60,30,.06);padding:2px 12px}
.row{height:21px;display:flex;align-items:center;font-size:8.3px;color:var(--body);border-bottom:1px solid var(--line)}
.row:last-child{border-bottom:none}
.row .view{margin-left:auto;font-size:6px;color:var(--muted);margin-right:7px}
.section{left:18px;top:256px;font-size:8.8px;font-weight:600;color:var(--green)}
.btn{left:14px;width:250px;height:30px;border-radius:15px;background:var(--green);color:#fff;font-size:8.5px;font-weight:600;display:flex;align-items:center;justify-content:center;box-shadow:0 6px 14px rgba(90,155,67,.32)}

/* create job */
.create{left:381px;top:612px;background:var(--surface)}
.brand-inline{left:16px;top:60px;font-size:13px;font-weight:700;letter-spacing:1px;color:var(--green-dark)}
.field{left:14px;width:250px;height:28px;border-radius:12px;background:#fff;border:1px solid var(--line);display:flex;align-items:center;padding:0 10px 0 5px;font-size:7px;color:var(--muted)}
.field-icon{width:19px;height:19px;border-radius:7px;background:var(--green-soft);display:flex;align-items:center;justify-content:center;margin-right:8px}
.field .chev{margin-left:auto}
.chips{left:14px;top:164px;width:250px;display:flex;gap:6px}
.chip{flex:1;height:22px;border-radius:11px;background:#fff;border:1px solid var(--line);display:flex;align-items:center;justify-content:center;gap:5px;font-size:6.3px;color:var(--muted)}
.chip i{width:7px;height:7px;border-radius:50%;border:1.2px solid var(--muted)}
.chip.on{border-color:var(--green);color:var(--green);background:var(--green-soft)}
.chip.on i{border:2.2px solid var(--green);background:#fff}
.box{top:196px;width:122px;height:28px;border:1px solid var(--line);border-radius:12px;background:#fff;font-size:7px;color:var(--muted);padding:0 12px;display:flex;align-items:center}
</style>
</head>
<body>

<!-- Splash -->
<section class="screen splash">
  <div class="abs splash-mark"></div>
  <div class="abs splash-name">HARVESTLY</div>
</section>

<!-- Home -->
<section class="screen home">
  <div class="abs title" style="left:18px;top:24px;font-size:14px">Home</div>
  <div class="abs avatar" role="img" aria-label="User profile photo" style="left:230px;top:18px;width:30px;height:30px;border:2px solid #fff;box-shadow:0 2px 6px rgba(0,0,0,.15)"></div>
  <div class="abs" style="left:252px;top:19px;width:8px;height:8px;border-radius:50%;background:#8fd15a;border:1.5px solid #fff"></div>

  <div class="abs tabs">
    <div class="tab active">Current Jobs For You</div>
    <div class="tab">Nearby Farmhands</div>
  </div>

  <div class="abs search">
    <svg width="9" height="9" viewBox="0 0 10 10"><circle cx="4" cy="4" r="3" fill="none" stroke="#8a9386" stroke-width="1.3"/><path d="M6.3 6.3 9 9" stroke="#8a9386" stroke-width="1.3"/></svg>
    search
    <div class="filter"><svg width="9" height="7" viewBox="0 0 9 7"><path d="M0 1h9M1.5 3.5h6M3 6h3" stroke="#fff" stroke-width="1.1" stroke-linecap="round"/></svg></div>
  </div>

  <div class="abs list">
    <article class="abs job" style="top:2px">
      <div class="abs job-icon"><svg width="16" height="16" viewBox="0 0 16 16" fill="none" stroke="var(--green)" stroke-width="1.2"><circle cx="8" cy="5" r="3"/><path d="M2 15c0-4 3-6 6-6s6 2 6 6z"/></svg></div>
      <div class="abs job-title">Seasional Farm Labour</div>
      <div class="abs job-meta" style="top:22px">Cedar Bend, Iowa</div>
      <div class="abs job-meta" style="top:31px">2.92 Miles &nbsp;•&nbsp; 08:00am - 08:00pm</div>
      <div class="abs job-heart"><svg width="12" height="11" viewBox="0 0 24 21"><path d="M12 21 2 11C-1 8 0 2 6 1c3 0 5 2 6 4 1-2 3-4 6-4 6 1 7 7 4 10z" fill="var(--heart)"/></svg></div>
      <div class="abs job-rule"></div>
      <div class="abs rate">Hourly Rate <b>$12 - 20</b></div>
      <div class="abs dates">Start Date: <span>April 01</span><br>End Date: <span>December 15</span></div>
    </article>

    <article class="abs job" style="top:80px">
      <div class="abs job-icon"><svg width="16" height="16" viewBox="0 0 16 16" fill="none" stroke="var(--green)" stroke-width="1.2"><path d="M1 4h9v7H1zM10 6h3l2 3v2h-5z"/><circle cx="4" cy="12.5" r="1.5"/><circle cx="12" cy="12.5" r="1.5"/></svg></div>
      <div class="abs job-title">Truck Driver</div>
      <div class="abs job-meta" style="top:22px">Cedar Bend, Iowa</div>
      <div class="abs job-meta" style="top:31px">2.92 Miles &nbsp;•&nbsp; 08:00am - 08:00pm</div>
      <div class="abs job-heart"><svg width="12" height="11" viewBox="0 0 24 21"><path d="M12 21 2 11C-1 8 0 2 6 1c3 0 5 2 6 4 1-2 3-4 6-4 6 1 7 7 4 10z" fill="none" stroke="#a3aa9f" stroke-width="2.2"/></svg></div>
      <div class="abs job-rule"></div>
      <div class="abs rate">Hourly Rate <b>$12 - 20</b></div>
      <div class="abs dates">Start Date: <span>March 01</span><br>End Date: <span>Feburary 28</span></div>
    </article>

    <article class="abs job" style="top:158px">
      <div class="abs job-icon"><svg width="16" height="16" viewBox="0 0 16 16" fill="none" stroke="var(--green)" stroke-width="1.2"><path d="M4 15V6M4 6V2h2v6M6 2V1h2v7M8 1h2v7M10 2h2v9l-2 4H4"/></svg></div>
      <div class="abs job-title">Farm Hand, Sprayer, Truck</div>
      <div class="abs job-meta" style="top:22px">Cedar Bend, Iowa</div>
      <div class="abs job-meta" style="top:31px">6.09 Miles &nbsp;•&nbsp; 08:00am - 08:00pm</div>
      <div class="abs job-heart"><svg width="12" height="11" viewBox="0 0 24 21"><path d="M12 21 2 11C-1 8 0 2 6 1c3 0 5 2 6 4 1-2 3-4 6-4 6 1 7 7 4 10z" fill="none" stroke="#a3aa9f" stroke-width="2.2"/></svg></div>
      <div class="abs job-rule"></div>
      <div class="abs rate">Hourly Rate <b>$16 - 22</b></div>
      <div class="abs dates">Start Date: <span>April 01</span><br>End Date: <span>December 15</span></div>
    </article>

    <article class="abs job" style="top:236px">
      <div class="abs job-icon" role="img" aria-label="Livestock job icon"></div>
      <div class="abs job-title">Sort And Lord Pigs</div>
      <div class="abs job-meta" style="top:22px">Cedar Bend, Iowa</div>
      <div class="abs job-meta" style="top:31px">6.09 Miles &nbsp;•&nbsp; 08:00am - 08:00pm</div>
      <div class="abs job-heart"><svg width="12" height="11" viewBox="0 0 24 21"><path d="M12 21 2 11C-1 8 0 2 6 1c3 0 5 2 6 4 1-2 3-4 6-4 6 1 7 7 4 10z" fill="none" stroke="#a3aa9f" stroke-width="2.2"/></svg></div>
      <div class="abs job-rule"></div>
      <div class="abs rate">Hourly Rate <b>$16 - 22</b></div>
      <div class="abs dates">Start Date: <span>April 01</span><br>End Date: <span>December 15</span></div>
    </article>

    <article class="abs job" style="top:314px">
      <div class="abs job-icon"><svg width="16" height="16" viewBox="0 0 16 16" fill="none" stroke="var(--green)" stroke-width="1.2"><path d="M4 15V6M4 6V2h2v6M6 2V1h2v7M8 1h2v7M10 2h2v9l-2 4H4"/></svg></div>
      <div class="abs job-title">Farm Hand, Sprayer, Truck</div>
      <div class="abs job-meta" style="top:22px">Cedar Bend, Iowa</div>
      <div class="abs job-meta" style="top:31px">6.09 Miles &nbsp;•&nbsp; 08:00am - 08:00pm</div>
      <div class="abs job-heart"><svg width="12" height="11" viewBox="0 0 24 21"><path d="M12 21 2 11C-1 8 0 2 6 1c3 0 5 2 6 4 1-2 3-4 6-4 6 1 7 7 4 10z" fill="none" stroke="#a3aa9f" stroke-width="2.2"/></svg></div>
      <div class="abs job-rule"></div>
    </article>
  </div>

  <nav class="abs nav">
    <div class="nav-active"><svg width="14" height="13" viewBox="0 0 17 15"><path d="M8.5 0 0 7.5h2.3V15h4.5v-4.5h3.4V15h4.5V7.5H17z" fill="#fff"/></svg></div>
    <svg width="14" height="14" viewBox="0 0 15 15"><circle cx="6" cy="6" r="4.6" fill="none" stroke="var(--icon)" stroke-width="1.6"/><path d="M9.5 9.5 14 14" stroke="var(--icon)" stroke-width="1.8" stroke-linecap="round"/></svg>
    <svg width="13" height="14" viewBox="0 0 14 15" fill="none" stroke="var(--icon)" stroke-width="1.2"><path d="M1 2h9v12H1z"/><path d="M4 1h9v12"/><path d="M3 6h5M3 8.5h5M3 11h5"/></svg>
    <svg width="13" height="15" viewBox="0 0 16 16" fill="none" stroke="var(--icon)" stroke-width="1.2"><path d="M4 15V6M4 6V2h2v6M6 2V1h2v7M8 1h2v7M10 2h2v9l-2 4H4"/></svg>
    <svg width="15" height="15" viewBox="0 0 16 16" fill="none" stroke="var(--icon)" stroke-width="1.2"><path d="M1 3h13v12H1zM1 6h13M4 1v3M11 1v3"/><circle cx="12" cy="12" r="3" fill="#fff"/><path d="M12 10.5V12h1.2"/></svg>
  </nav>
</section>

<!-- Profile -->
<section class="screen profile">
  <div class="abs back"><svg width="6" height="9" viewBox="0 0 5 8"><path d="M4.5.5 1 4l3.5 3.5" fill="none" stroke="var(--ink)" stroke-width="1.3" stroke-linecap="round"/></svg></div>
  <div class="abs title" style="left:54px;top:27px">My Profile</div>

  <div class="abs banner"></div>
  <div class="abs avatar" role="img" aria-label="Profile photo of Daniel Whitford" style="left:24px;top:75px;width:44px;height:44px;border:2px solid #fff"></div>
  <div class="abs online"></div>
  <div class="abs p-name">Daniel Whitford</div>
  <div class="abs p-sub" style="top:93px">Founder \ C.E.O</div>
  <div class="abs p-sub" style="top:104px">5550142876</div>
  <div class="abs rating"><svg width="8" height="8" viewBox="0 0 10 10"><path d="m5 0 1.5 3.3 3.5.4-2.6 2.4.7 3.5L5 7.8 1.9 9.6l.7-3.5L0 3.7l3.5-.4z" fill="var(--star)"/></svg>5.0</div>

  <div class="abs group" style="top:148px">
    <div class="row">User Details<span class="view">View Details</span><svg width="4" height="7" viewBox="0 0 4 7"><path d="M.5.5 3.5 3.5.5 6.5" fill="none" stroke="var(--green)" stroke-width="1.1"/></svg></div>
    <div class="row">Education Details<span class="view">View Details</span><svg width="4" height="7" viewBox="0 0 4 7"><path d="M.5.5 3.5 3.5.5 6.5" fill="none" stroke="var(--green)" stroke-width="1.1"/></svg></div>
    <div class="row">Farm Details<span class="view">View Details</span><svg width="4" height="7" viewBox="0 0 4 7"><path d="M.5.5 3.5 3.5.5 6.5" fill="none" stroke="var(--green)" stroke-width="1.1"/></svg></div>
    <div class="row">Farm Images<span class="view">View Details</span><svg width="4" height="7" viewBox="0 0 4 7"><path d="M.5.5 3.5 3.5.5 6.5" fill="none" stroke="var(--green)" stroke-width="1.1"/></svg></div>
  </div>

  <div class="abs section">Harvestly Jobs</div>

  <div class="abs group" style="top:274px">
    <div class="row">Applied Jobs<span class="view">View Details</span><svg width="4" height="7" viewBox="0 0 4 7"><path d="M.5.5 3.5 3.5.5 6.5" fill="none" stroke="var(--green)" stroke-width="1.1"/></svg></div>
    <div class="row">Scheduled Jobs<span class="view">View Details</span><svg width="4" height="7" viewBox="0 0 4 7"><path d="M.5.5 3.5 3.5.5 6.5" fill="none" stroke="var(--green)" stroke-width="1.1"/></svg></div>
    <div class="row">Received Jobs<span class="view">View Details</span><svg width="4" height="7" viewBox="0 0 4 7"><path d="M.5.5 3.5 3.5.5 6.5" fill="none" stroke="var(--green)" stroke-width="1.1"/></svg></div>
    <div class="row">Favourite Jobs<span class="view">View Details</span><svg width="4" height="7" viewBox="0 0 4 7"><path d="M.5.5 3.5 3.5.5 6.5" fill="none" stroke="var(--green)" stroke-width="1.1"/></svg></div>
    <div class="row">Completed Jobs<span class="view">View Details</span><svg width="4" height="7" viewBox="0 0 4 7"><path d="M.5.5 3.5 3.5.5 6.5" fill="none" stroke="var(--green)" stroke-width="1.1"/></svg></div>
    <div class="row">Scheduled Jobs<span class="view">View Details</span><svg width="4" height="7" viewBox="0 0 4 7"><path d="M.5.5 3.5 3.5.5 6.5" fill="none" stroke="var(--green)" stroke-width="1.1"/></svg></div>
    <div class="row">Received Jobs<span class="view">View Details</span><svg width="4" height="7" viewBox="0 0 4 7"><path d="M.5.5 3.5 3.5.5 6.5" fill="none" stroke="var(--green)" stroke-width="1.1"/></svg></div>
  </div>

  <div class="abs btn" style="top:446px">Logout</div>
</section>

<!-- Create New Job -->
<section class="screen create">
  <div class="abs back"><svg width="6" height="9" viewBox="0 0 5 8"><path d="M4.5.5 1 4l3.5 3.5" fill="none" stroke="var(--ink)" stroke-width="1.3" stroke-linecap="round"/></svg></div>
  <div class="abs title" style="left:54px;top:27px">Create New Job</div>
  <div class="abs brand-inline">HARVESTLY</div>

  <div class="abs field" style="top:88px"><span class="field-icon"><svg width="10" height="8" viewBox="0 0 11 9" fill="none" stroke="var(--green)" stroke-width="1"><path d="M.5 2.5h10v6H.5zM3.5 2.5V.5h4v2M.5 5h10"/></svg></span>Job Category<svg class="chev" width="7" height="4" viewBox="0 0 6 4"><path d="M.5.5 3 3 5.5.5" fill="none" stroke="#8a9386" stroke-width=".9"/></svg></div>
  <div class="abs field" style="top:126px"><span class="field-icon"><svg width="10" height="8" viewBox="0 0 11 9" fill="none" stroke="var(--green)" stroke-width="1"><path d="M.5 2.5h10v6H.5zM3.5 2.5V.5h4v2M.5 5h10"/></svg></span>Job Title<svg class="chev" width="7" height="4" viewBox="0 0 6 4"><path d="M.5.5 3 3 5.5.5" fill="none" stroke="#8a9386" stroke-width=".9"/></svg></div>

  <div class="abs chips">
    <div class="chip on"><i></i>Hourly Rate ($)</div>
    <div class="chip"><i></i>Fixed Salary ($)</div>
    <div class="chip"><i></i>Per Acre ($)</div>
  </div>

  <div class="abs box" style="left:14px">From</div>
  <div class="abs box" style="left:142px">To</div>

  <div class="abs field" style="top:238px"><span class="field-icon"><svg width="10" height="8" viewBox="0 0 11 9" fill="none" stroke="var(--green)" stroke-width="1"><path d="M.5 2.5h10v6H.5zM3.5 2.5V.5h4v2M.5 5h10"/></svg></span>Job Type<svg class="chev" width="7" height="4" viewBox="0 0 6 4"><path d="M.5.5 3 3 5.5.5" fill="none" stroke="#8a9386" stroke-width=".9"/></svg></div>
  <div class="abs field" style="top:276px"><span class="field-icon"><svg width="10" height="8" viewBox="0 0 11 9" fill="none" stroke="var(--green)" stroke-width="1"><path d="M.5 2.5h10v6H.5zM3.5 2.5V.5h4v2M.5 5h10"/></svg></span>Equipment Provided<svg class="chev" width="7" height="4" viewBox="0 0 6 4"><path d="M.5.5 3 3 5.5.5" fill="none" stroke="#8a9386" stroke-width=".9"/></svg></div>
  <div class="abs field" style="top:314px"><span class="field-icon"><svg width="10" height="8" viewBox="0 0 11 9" fill="none" stroke="var(--green)" stroke-width="1"><path d="M.5 2.5h10v6H.5zM3.5 2.5V.5h4v2M.5 5h10"/></svg></span>Start Date and Time<svg class="chev" width="7" height="4" viewBox="0 0 6 4"><path d="M.5.5 3 3 5.5.5" fill="none" stroke="#8a9386" stroke-width=".9"/></svg></div>
  <div class="abs field" style="top:352px"><span class="field-icon"><svg width="10" height="8" viewBox="0 0 11 9" fill="none" stroke="var(--green)" stroke-width="1"><path d="M.5 2.5h10v6H.5zM3.5 2.5V.5h4v2M.5 5h10"/></svg></span>End Date and Time<svg class="chev" width="7" height="4" viewBox="0 0 6 4"><path d="M.5.5 3 3 5.5.5" fill="none" stroke="#8a9386" stroke-width=".9"/></svg></div>

  <div class="abs btn" style="top:430px">Logout</div>
</section>

</body>
</html>
```